Mobile Recording Studio needs business cards

Open to seeing a creative design, but I want to emphasis my logo and minimize the name/title and company information. Possible a fully black background on card.

My company is a mobile sound recording studio. ok to include a my trailer (actual or cartoon) on the card. My initial thought is more straight forward, but a good design will win me over.

SPECS:
CMYK color mode
High (300ppi) raster effect.
cover bleed area
please deliver: Illustrator file with layers and a pdf at completion.

Name and info for the business card:

Dallin Perry
ADR Mixer

email: Dallin@MixVault.com

address:
248 - 5170 East Hollister
Vancouver, BC V5R 2J4

phone:
604.518.2093 office

website:
www.MixVault.com

FB: @MixVault

Instagram: @TheMixVault

Industry/Entity Type

Television Production

Contact Information for Business Card

Dallin Perry
ADR Mixer

email: Dallin@MixVault.com

address:
248 - 5170 East Hollister
Vancouver, BC V5R 2J4

phone:
604.518.2093 office

website:
www.MixVault.com

FB: @MixVault

Instagram: @TheMixVault

Colors

Designer to choose colors to be used in the design.

Requirements
Must have
• emphasis my logo and minimize the name/title and company information.
• SPECS:
• CMYK color mode
• High (300ppi) raster effect.
• cover bleed area
• please deliver: Illustrator file with layers and a pdf at completion.
Nice to have
• maybe include the following:
• all black background or black theme
• my work trailer (actual or cartoon) refer to Instagram: @TheMixVault

```html
<!DOCTYPE html>
<html lang="en">
<head>
<meta charset="utf-8">
<title>MixVault Business Card</title>
<link rel="stylesheet" href="https://fonts.googleapis.com/css2?family=Libre+Baskerville:wght@700&family=Montserrat:wght@500&display=swap">
<style>
  :root {
    --backdrop: #2a2a2c;
    --card: #1e1e1f;
    --silver: #c9c9cc;
    --text: #f2f2f2;
    --panel: #ffffff;
    --photo-dark: #141414;
    --photo-mid: #3a3a3c;
  }
  * { box-sizing: border-box; margin: 0; padding: 0; }
  html, body { width: 1200px; height: 900px; overflow: hidden; }
  body {
    background: var(--backdrop);
    display: flex;
    flex-direction: column;
    align-items: center;
    justify-content: center;
    gap: 34px;
  }
  .card {
    position: relative;
    width: 700px;
    height: 400px;
    background: var(--card);
    overflow: hidden;
  }
  .card-front {
    display: flex;
    align-items: center;
    justify-content: center;
  }
  .brand-name {
    font-family: "Libre Baskerville", Georgia, serif;
    font-weight: 700;
    font-size: 92px;
    color: var(--silver);
    letter-spacing: -1px;
  }
  .card-back { color: var(--text); }
  .contact-block {
    position: absolute;
    left: 56px;
    top: 60px;
    font-family: "Montserrat", Arial, sans-serif;
    font-weight: 500;
  }
  .person-name {
    font-family: "Libre Baskerville", Georgia, serif;
    font-weight: 700;
    font-size: 22px;
    letter-spacing: 2px;
    text-transform: uppercase;
  }
  .person-title { font-size: 14px; letter-spacing: 1px; margin: 2px 0 0 2px; }
  .address { font-size: 13px; letter-spacing: 1.2px; line-height: 1.55; margin-top: 30px; }
  .contact-list { list-style: none; margin-top: 20px; font-size: 13px; letter-spacing: 1px; }
  .contact-list li { display: flex; align-items: center; gap: 10px; height: 24px; }
  .contact-list svg { width: 16px; height: 16px; flex: none; }
  .social-list {
    list-style: none;
    display: flex;
    gap: 62px;
    margin-top: 26px;
    font-size: 13px;
    letter-spacing: 1px;
  }
  .social-list li { display: flex; align-items: center; gap: 8px; }
  .social-mark {
    width: 16px; height: 16px;
    border: 1.6px solid var(--text);
    border-radius: 4px;
  }
  .trailer-panel { position: absolute; right: 0; top: 0; width: 380px; height: 400px; }
</style>
</head>
<body>
  <section class="card card-front">
    <span class="brand-name">MixVault</span>
  </section>

  <section class="card card-back">
    <div class="contact-block">
      <h1 class="person-name">Dallin Perry</h1>
      <p class="person-title">ADR Mixer</p>
      <p class="address">248 - 5170 East Hollister<br>Vancouver, BC V5R 2J4</p>
      <ul class="contact-list">
        <li>
          <svg viewBox="0 0 16 16" fill="none" stroke="currentColor" stroke-width="1.3"><rect x="4" y="1" width="8" height="14" rx="1.5"/><line x1="7" y1="12.5" x2="9" y2="12.5"/></svg>
          604.518.2093
        </li>
        <li>
          <svg viewBox="0 0 16 16" fill="none" stroke="currentColor" stroke-width="1.3"><rect x="1" y="3.5" width="14" height="9"/><path d="M1 3.5 L8 9 L15 3.5"/></svg>
          Dallin@MixVault.com
        </li>
        <li>
          <svg viewBox="0 0 16 16" fill="none" stroke="currentColor" stroke-width="1.2"><circle cx="8" cy="8" r="6.5"/><ellipse cx="8" cy="8" rx="3" ry="6.5"/><line x1="1.5" y1="8" x2="14.5" y2="8"/></svg>
          www.MixVault.com
        </li>
      </ul>
      <ul class="social-list">
        <li><span class="social-mark"></span>TheMixVault</li>
        <li><span class="social-mark"></span>MixVault</li>
      </ul>
    </div>

    <svg class="trailer-panel" viewBox="0 0 380 400" role="img" aria-label="Photo of the black mobile recording studio trailer with its side door">
      <defs>
        <linearGradient id="trailerTone" x1="0" y1="0" x2="1" y2="1">
          <stop offset="0" stop-color="var(--photo-mid)"/>
          <stop offset="1" stop-color="var(--photo-dark)"/>
        </linearGradient>
      </defs>
      <path d="M120 0 H380 V400 H60 C10 330 0 220 30 130 C50 70 85 25 120 0 Z" fill="var(--panel)"/>
      <rect x="70" y="60" width="310" height="260" fill="url(#trailerTone)"/>
    </svg>
  </section>
</body>
</html>
```